Simple and elegant Wallsaver Packaging needed for our new product

We are looking for a packaging for our new wallsaver product, which primary purpose is to protect damages to the wall. It prevents drilling holes into the wall.

Packaging file can be found - https://files.plorvex.net/open?id=7Kzq2RTmwobNXvLcaHyuPEsjDfG

The company name is Dornaby and i have attached pictures of the product and the company logo that we would like on the packaging.

Examples of packaging we like in terms of packaging are tavsen packaging and frome & lattis packaging.

Copies of instructions to set up the product are on the 5th picture on this link - https://www.shopvarro.co.uk/d/kpt/Belvo-Pressure-Guard-Surface-Gates-Curtain-Tension-Mounted/Z73K4WQM2J.
Updates

All,I have updated the brief and add more info about the packaging so please have another look.I look forward to receiving your designs and giving feedback.Thanks Added Thursday, January 12, 2017

Hi All, We still awaiting for more entries before making our final decision. Happy to assist if anyone has further queries. Thanks

One more day left so please submit your designs. I will be giving feedback shortly on the designs received so far. A few designers have asked for me to extend the competition so they have time to submit, so i may do this. Regards Tesk

Reason: Hi, I am extending the deadline so designers can incorporate the feedback i am going to give. So i can get the best possible design possible. Thanks

Target Market(s)

Homeowners

Industry/Entity Type

Home Improvement

Requirements
Must have
• Logo, Instructions to use
Nice to have
• Pictures of product

```html
<!DOCTYPE html>
<html lang="en">
<head>
<meta charset="utf-8">
<title>Dornaby Pressure Gate Wall Saver – Packaging</title>
<link rel="stylesheet" href="https://fonts.googleapis.com/css2?family=Oswald:wght@300;400;500&family=Arimo:wght@400&display=swap">
<style>
  :root {
    --teal: #1bbcc0;
    --teal-deep: #10a5a8;
    --panel: #f5f6f6;
    --badge: #e4e5e5;
    --badge-ring: #c9caca;
    --ink: #4d4f50;
    --ink-soft: #6b6d6e;
    --product-light: #e6e4de;
    --product-dark: #9c9d9c;
    --stage: #e8ebec;
    --cloud: #bfe3e2;
  }
  * { box-sizing: border-box; margin: 0; padding: 0; }
  html, body { width: 1028px; height: 1200px; overflow: hidden; }
  body {
    background: var(--stage);
    font-family: "Arimo", Arial, sans-serif;
    color: var(--ink);
    position: relative;
  }
  .dieline {
    position: absolute;
    left: 189px;
    display: flex;
    height: 560px;
  }
  .dieline--front { top: 25px; }
  .dieline--back { top: 615px; }

  /* Spine */
  .spine {
    width: 210px;
    height: 100%;
    background: var(--teal);
    display: flex;
    flex-direction: column;
    align-items: center;
    padding-top: 40px;
  }
  .brand {
    font-family: "Oswald", sans-serif;
    font-weight: 300;
    color: #fff;
    text-align: center;
    line-height: 1;
  }
  .brand__name { letter-spacing: 0.06em; text-transform: uppercase; }
  .brand__tag {
    display: block;
    font-size: 7px;
    letter-spacing: 0.22em;
    margin-top: 5px;
  }
  .spine .brand__name { font-size: 34px; }
  .spine__badges {
    display: flex;
    flex-direction: column;
    gap: 16px;
    margin-top: 22px;
  }
  .disc {
    width: 108px;
    height: 108px;
    border-radius: 50%;
    background: #fff;
    border: 3px solid #dff4f4;
    display: flex;
    align-items: center;
    justify-content: center;
    overflow: hidden;
  }
  .disc__photo {
    width: 76px;
    height: 76px;
    border-radius: 50%;
    background: radial-gradient(circle at 55% 55%, var(--product-light) 0 45%, var(--product-dark) 70%, #fff 72%);
  }
  .disc__photo--mounted {
    background: radial-gradient(circle at 50% 50%, #fdfdfd 0 40%, #e2e3e3 55%, #fff 70%);
  }
  .product-title {
    font-family: "Oswald", sans-serif;
    font-weight: 300;
    text-transform: uppercase;
    text-align: center;
    color: var(--ink);
    line-height: 1.05;
  }
  .disc .product-title { font-size: 16px; }
  .disc .product-title span { display: block; }
  .disc .product-title .big { font-size: 21px; }
  .spine__count {
    margin-top: auto;
    margin-bottom: 30px;
    font-family: "Oswald", sans-serif;
    font-weight: 500;
    color: #fff;
    font-size: 19px;
  }

  /* Main faces */
  .face {
    width: 440px;
    height: 100%;
    background: var(--panel);
    position: relative;
    overflow: hidden;
  }
  .logo-block {
    position: absolute;
    top: 30px;
    left: 95px;
    width: 270px;
    height: 160px;
    background: var(--teal-deep);
    display: flex;
    align-items: center;
    justify-content: center;
  }
  .logo-block .brand__name { font-size: 46px; }
  .logo-block .brand__tag { font-size: 9px; margin-top: 8px; }

  .face__band {
    position: absolute;
    left: 0; right: 0;
    top: 410px;
    height: 30px;
    background: var(--teal);
  }
  .face__product {
    position: absolute;
    left: 100px;
    top: 300px;
    width: 220px;
    height: 240px;
    border-radius: 50%;
    background: radial-gradient(circle at 62% 58%, #f1efea 0 32%, var(--product-light) 55%, var(--product-dark) 75%, rgba(156,157,156,0) 77%);
  }
  .seal {
    position: absolute;
    right: 22px;
    top: 180px;
    width: 140px;
    height: 140px;
    border-radius: 50%;
    background: var(--badge);
    border: 2px solid #d6d7d7;
    display: flex;
    align-items: center;
    justify-content: center;
  }
  .seal::before {
    content: "";
    position: absolute;
    inset: 8px;
    border-radius: 50%;
    border: 1px dashed var(--badge-ring);
  }
  .seal .product-title { font-size: 23px; }
  .seal .product-title span { display: block; }
  .seal .product-title .big { font-size: 31px; }
  .face__count {
    position: absolute;
    left: 22px;
    top: 462px;
    font-family: "Oswald", sans-serif;
    font-weight: 500;
    font-size: 24px;
    color: var(--ink);
  }
  .subline {
    position: absolute;
    right: 14px;
    top: 394px;
    width: 100px;
    height: 62px;
    border-radius: 31px;
    background: var(--cloud);
    display: flex;
    align-items: center;
    justify-content: center;
    gap: 6px;
    font-family: "Oswald", sans-serif;
    font-weight: 300;
    font-size: 18px;
    color: var(--teal-deep);
  }
  .subline__dot {
    width: 10px; height: 10px; border-radius: 50%;
    background: var(--teal-deep);
  }

  /* Back */
  .features {
    position: absolute;
    top: 225px;
    left: 28px;
    right: 30px;
    list-style: none;
    display: flex;
    flex-direction: column;
    gap: 26px;
  }
  .features li {
    position: relative;
    padding-left: 16px;
    font-size: 13px;
    line-height: 1.4;
    color: var(--teal-deep);
  }
  .features li::before {
    content: "";
    position: absolute;
    left: 0; top: 5px;
    width: 7px; height: 7px;
    border-radius: 50%;
    background: #d3d5d5;
  }
  .features li.features__last { padding-right: 110px; }
  .features__photo {
    position: absolute;
    right: 40px;
    bottom: 62px;
    width: 62px;
    height: 70px;
    border-radius: 50%;
    background: radial-gradient(circle at 58% 58%, #f1efea 0 30%, var(--product-light) 50%, var(--product-dark) 72%, rgba(156,157,156,0) 74%);
  }
  .origin {
    position: absolute;
    left: 28px;
    bottom: 22px;
    font-size: 11px;
    color: var(--ink-soft);
  }
</style>
</head>
<body>

<section class="dieline dieline--front" aria-label="Spine and front face">
  <aside class="spine">
    <div class="brand"><span class="brand__name">Dornaby</span><span class="brand__tag">HOMEWARE ACCESSORIES</span></div>
    <div class="spine__badges">
      <div class="disc"><div class="disc__photo" role="img" aria-label="Photo of the wall saver pad, front and rubber back"></div></div>
      <div class="disc"><div class="disc__photo disc__photo--mounted" role="img" aria-label="Photo of the wall saver pad fitted to a gate spindle"></div></div>
      <div class="disc"><p class="product-title"><span>Pressure</span><span>Gate Wall</span><span class="big">Saver</span></p></div>
    </div>
    <p class="spine__count">2 PACK</p>
  </aside>

  <article class="face face--front">
    <div class="logo-block"><div class="brand"><span class="brand__name">Dornaby</span><span class="brand__tag">HOMEWARE ACCESSORIES</span></div></div>
    <div class="face__band"></div>
    <div class="face__product" role="img" aria-label="Photo of two grey wall saver pads, one showing the ribbed rubber back"></div>
    <div class="seal"><p class="product-title"><span>Pressure</span><span>Gate Wall</span><span class="big">Saver</span></p></div>
    <div class="subline"><span class="subline__dot"></span>Nestling</div>
    <p class="face__count">2 PACK</p>
  </article>
</section>

<section class="dieline dieline--back" aria-label="Spine and back face">
  <aside class="spine">
    <div class="brand"><span class="brand__name">Dornaby</span><span class="brand__tag">HOMEWARE ACCESSORIES</span></div>
    <div class="spine__badges">
      <div class="disc"><div class="disc__photo" role="img" aria-label="Photo of the wall saver pad, front and rubber back"></div></div>
      <div class="disc"><div class="disc__photo disc__photo--mounted" role="img" aria-label="Photo of the wall saver pad fitted to a gate spindle"></div></div>
      <div class="disc"><p class="product-title"><span>Pressure</span><span>Gate Wall</span><span class="big">Saver</span></p></div>
    </div>
    <p class="spine__count">2 PACK</p>
  </aside>

  <article class="face face--back">
    <div class="logo-block"><div class="brand"><span class="brand__name">Dornaby</span><span class="brand__tag">HOMEWARE ACCESSORIES</span></div></div>
    <ul class="features">
      <li>Easy Fast Installation, No Tools Required, Used for Pressure Mounted Gate.</li>
      <li>Oversized Pad Protects Walls Better, Large Surface Area and Rubber Backing Pad with Little Suckers Make For More Stable Installation And More Security.</li>
      <li>Use on Top Spindles Only - Not Needed on Doorways With Doors Installed.</li>
      <li class="features__last">Thick Pad Equalizes Distance From The Top to Bottom of Gate.</li>
    </ul>
    <div class="features__photo" role="img" aria-label="Small photo of a wall saver pad"></div>
    <p class="origin">Made in China</p>
  </article>
</section>

</body>
</html>
```